" Somos um grupo de Psiquiatras que atende em domicílio e hospitais. Funcionamos em escala de sobreaviso. Normalmente fazemos visitas para pacientes que por alguma limitação ou urgência não podem ser atendidos em consultório. "

```html
<!DOCTYPE html>
<html lang="pt-BR">
<head>
<meta charset="UTF-8">
<title>Equipe Alvorada — Cartão de visita</title>
<link href="https://fonts.googleapis.com/css2?family=Arimo:wght@400;700&display=swap" rel="stylesheet">
<style>
  :root {
    --page-bg: #e6e4e0;
    --navy-top: #1c2c54;
    --navy-mid: #14213f;
    --navy-low: #1a2a50;
    --accent-line: #5ea3df;
    --ink-light: #f1ede4;
    --ink-soft: #e4e8f0;
    --icon-blue: #6fb1e8;
  }
  * { margin: 0; padding: 0; box-sizing: border-box; }
  html, body {
    width: 1200px;
    height: 1200px;
    overflow: hidden;
    background: var(--page-bg);
  }
  .canvas {
    position: relative;
    width: 1200px;
    height: 1200px;
  }
  .business-card {
    position: absolute;
    left: 100px;
    top: 322px;
    width: 1000px;
    height: 556px;
    overflow: hidden;
    background: var(--navy-low);
    box-shadow: 0 10px 30px rgba(0,0,0,0.18);
  }
  .band-top {
    position: absolute;
    left: 0; top: 0;
    width: 100%; height: 190px;
    background: var(--navy-top);
  }
  .band-middle {
    position: absolute;
    left: 0; top: 190px;
    width: 100%; height: 152px;
    background: var(--navy-mid);
  }
  .accent-rule {
    position: absolute;
    left: 0; top: 342px;
    width: 100%; height: 6px;
    background: var(--accent-line);
  }
  .brand {
    position: absolute;
    right: 70px;
    top: 208px;
    text-align: right;
  }
  .brand-name {
    font-family: "Arimo", sans-serif;
    font-size: 80px;
    line-height: 1;
    font-weight: 700;
    color: var(--ink-light);
  }
  .brand-tagline {
    margin-top: 12px;
    font-family: "Arimo", sans-serif;
    font-size: 22px;
    font-weight: 400;
    color: var(--ink-light);
  }
  .contact-list {
    position: absolute;
    left: 0;
    top: 388px;
    width: 100%;
    list-style: none;
    font-family: "Arimo", sans-serif;
    font-size: 30px;
    color: var(--ink-soft);
  }
  .contact-item {
    display: flex;
    justify-content: center;
    align-items: center;
    gap: 10px;
    height: 48px;
  }
  .contact-icon {
    width: 24px;
    height: 24px;
    flex: none;
  }
</style>
</head>
<body>
<main class="canvas">
  <section class="business-card">
    <div class="band-top"></div>
    <div class="band-middle"></div>
    <div class="accent-rule"></div>

    <header class="brand">
      <h1 class="brand-name">Equipe Alvorada</h1>
      <p class="brand-tagline">Cuidados em psiquiatria</p>
    </header>

    <ul class="contact-list">
      <li class="contact-item">
        <svg class="contact-icon" viewBox="0 0 24 24" aria-hidden="true">
          <path d="M12 2a7 7 0 0 0-7 7c0 5.2 7 13 7 13s7-7.8 7-13a7 7 0 0 0-7-7zm0 9.6a2.6 2.6 0 1 1 0-5.2 2.6 2.6 0 0 1 0 5.2z" fill="var(--icon-blue)"/>
        </svg>
        <span>Atendimento domiciliar e hospitalar</span>
      </li>
      <li class="contact-item">
        <svg class="contact-icon" viewBox="0 0 24 24" aria-hidden="true">
          <path d="M6.6 10.8a15.2 15.2 0 0 0 6.6 6.6l2.2-2.2a1 1 0 0 1 1-.25 11.4 11.4 0 0 0 3.6.57 1 1 0 0 1 1 1V20a1 1 0 0 1-1 1A17 17 0 0 1 3 4a1 1 0 0 1 1-1h3.5a1 1 0 0 1 1 1c0 1.25.2 2.45.57 3.6a1 1 0 0 1-.25 1z" fill="var(--icon-blue)"/>
        </svg>
        <span>(81) 990001234</span>
      </li>
    </ul>
  </section>
</main>
</body>
</html>
```